Rivolex.com Trucking Company Website

Need a website designed (no content) for a trucking company, specializing in trucking of ocean containers (intermodal Trucking). Heavy emphasis on technology, using latest technology, providing unabated visibility and realtime information.
clean minimalist industrial website
example:
https://www.bramtiq.com/

Target Market(s)

Professional Business Consumer corporate and small business

Industry/Entity Type

Trucking Company

Number of Pages Required

5+ page

Requirements
Must have
• Industrial Design, simple informative, for a busy professional to view and get the necessary information with out the distractions.
• Blog Page
• Client Log-In on the front page
• Technology page - showing our intensive investments in technology
Nice to have
• If ANY images included, MUST be USA related. Example if include an image of a truck, ensure its a USA model. Do the research.
• included our business card for sample of Logo
• Doesnt not have to be the same color schemes.
Should not have
• moving images

```html
<!DOCTYPE html>
<html lang="en">
<head>
<meta charset="utf-8">
<title>Rivolex Consulting</title>
<link rel="stylesheet" href="https://fonts.googleapis.com/css2?family=Lato:wght@400;700&family=Play:wght@700&display=swap">
<style>
:root{
  --blue:#155a9c;
  --blue-dark:#0f4a85;
  --black:#050505;
  --ink:#333333;
  --text:#444444;
  --white:#ffffff;
  --card:#f8f8f8;
  --line:#dddddd;
}
*{box-sizing:border-box;margin:0;padding:0}
html,body{width:1200px;height:1040px;overflow:hidden;background:var(--white);font-family:'Lato',sans-serif}
.page{position:relative;width:1200px;height:1040px}
.topline{position:absolute;left:0;top:0;width:1200px;height:3px;background:var(--blue);z-index:3}
.hero{position:absolute;left:0;top:0;width:1200px;height:626px;
  background:radial-gradient(ellipse at 60% 45%,#6a6a6a 0%,#3a3a3a 35%,#151515 65%,#0c1d33 100%)}
.brand{position:absolute;left:99px;top:24px;color:var(--white);font-family:'Play',sans-serif;font-weight:700;z-index:2}
.brand-name{font-size:44px;letter-spacing:2px;line-height:46px;display:block}
.brand-sub{font-size:17px;letter-spacing:8.6px;line-height:20px;display:block}
.nav{position:absolute;top:31px;left:660px;height:40px;display:flex;align-items:center;z-index:2}
.nav a{color:var(--white);text-decoration:none;font-size:15px;letter-spacing:.4px;font-family:'Lato',sans-serif}
.nav .sep{width:1px;height:16px;background:#777;margin:0 33px}
.nav .sep.tall{height:40px;margin:0 32px 0 36px}
.login{display:flex;align-items:center;gap:7px;width:154px;height:40px;justify-content:center;border:1px solid #6fa3d9;background:var(--blue)}
.hero-mark{position:absolute;left:582px;top:120px;color:var(--blue);font-family:'Play',sans-serif;font-weight:700;font-size:26px;letter-spacing:1px}
.headline{position:absolute;left:0;top:484px;width:1200px;text-align:center;color:var(--white);font-family:'Play',sans-serif;font-weight:700;font-size:44px;letter-spacing:.5px;text-shadow:0 2px 6px rgba(0,0,0,.5)}
.panel{position:absolute;left:99px;top:575px;width:1002px;height:342px;background:var(--white);box-shadow:0 0 18px rgba(0,0,0,.12)}
.card{position:absolute;top:603px;width:300px;height:278px;background:var(--card);border:1px solid var(--line);text-align:center}
.card h2{margin-top:25px;font-family:'Play',sans-serif;font-weight:700;font-size:21px;color:var(--ink);letter-spacing:.3px}
.card .icon{width:122px;height:122px;margin:14px auto 0;border-radius:50%;background:var(--blue);border:4px solid var(--white);box-shadow:0 0 0 3px var(--blue);display:flex;align-items:center;justify-content:center}
.card p{margin:22px auto 0;width:240px;font-size:12.5px;line-height:19.5px;color:var(--text)}
.card.active{background:linear-gradient(180deg,#4b7fb8 0%,#3571ad 55%,#2f6aa6 100%);border:9px solid var(--blue)}
.card.active::after{content:"";position:absolute;inset:0;border:2px solid var(--white)}
.card.active h2{margin-top:16px;color:var(--white)}
.card.active p{color:var(--white)}
.card.active .icon{box-shadow:0 0 0 3px #c9d7e6}
.contact{position:absolute;left:0;top:942px;width:1200px;height:55px;background:var(--black);display:flex;align-items:center;justify-content:center;gap:36px;color:var(--white);font-size:15px}
.contact span{display:flex;align-items:center;gap:10px}
.legal{position:absolute;left:0;top:997px;width:1200px;height:43px;background:var(--blue)}
.legal p{position:absolute;left:99px;top:13px;color:var(--white);font-size:13.5px;font-weight:700}
.social{position:absolute;right:98px;top:6px;display:flex;gap:7px}
.social i{display:block;width:28px;height:28px;border-radius:50%;background:var(--white)}
</style>
</head>
<body>
<div class="page">
  <div class="topline"></div>
  <div class="hero" role="img" aria-label="Businessman touching a glowing world map with connected network lines"></div>

  <div class="brand"><span class="brand-name">RIVOLEX</span><span class="brand-sub">CONSULTING</span></div>

  <nav class="nav">
    <a href="#">BLOG</a><span class="sep"></span>
    <a href="#">TECHNOLOGY</a><span class="sep tall"></span>
    <a href="#" class="login">
      <svg width="16" height="14" viewBox="0 0 16 14"><path d="M0 5h6V2l5 5-5 5V9H0z" fill="#fff"/><path d="M9 1h6v12H9" fill="none" stroke="#fff" stroke-width="2"/></svg>
      CLIENT LOGIN</a>
  </nav>

  <div class="hero-mark">RIVOLEX</div>
  <h1 class="headline">TECHNOLOGY DRIVEN COMPANY</h1>

  <div class="panel"></div>

  <section class="card" style="left:124px">
    <h2>INTERMODAL TRUCKING</h2>
    <div class="icon">
      <svg width="56" height="62" viewBox="0 0 56 62" fill="#fff"><rect x="12" y="0" width="32" height="6"/><rect x="6" y="8" width="44" height="30" rx="3"/><rect x="12" y="13" width="32" height="12" fill="#155a9c"/><rect x="0" y="16" width="5" height="8"/><rect x="51" y="16" width="5" height="8"/><rect x="4" y="40" width="48" height="10" rx="2"/><rect x="18" y="32" width="20" height="8" fill="#155a9c"/><rect x="6" y="52" width="10" height="8"/><rect x="40" y="52" width="10" height="8"/></svg>
    </div>
    <p>Lorem ipsum dolor sit amet, consectetuer adipiscing elit,sed consectetuer adipiscing elit,sed diam nonummy.</p>
  </section>

  <section class="card active" style="left:450px" role="img" aria-label="Row of American freight trucks at a terminal">
    <h2>LTL</h2>
    <div class="icon">
      <svg width="70" height="46" viewBox="0 0 70 46"><path d="M0 4a4 4 0 0 1 4-4h40v34H0z" fill="#fff"/><path d="M46 10h12l10 12v12H46z" fill="#fff"/><circle cx="14" cy="36" r="8" fill="#fff" stroke="#155a9c" stroke-width="3"/><circle cx="56" cy="36" r="8" fill="#fff" stroke="#155a9c" stroke-width="3"/><text x="22" y="22" text-anchor="middle" font-family="Play,sans-serif" font-weight="700" font-size="17" fill="#155a9c">LTL</text></svg>
    </div>
    <p>Lorem ipsum dolor sit amet, consectetuer adipiscing elit,sed consectetuer adipiscing elit,sed diam nonummy.</p>
  </section>

  <section class="card" style="left:777px">
    <h2>WAREHOUSING</h2>
    <div class="icon">
      <svg width="62" height="52" viewBox="0 0 62 52" fill="#fff"><path d="M31 0 62 14v4H0v-4z"/><rect x="4" y="20" width="54" height="32"/><rect x="12" y="24" width="38" height="28" fill="#155a9c"/><rect x="15" y="27" width="32" height="2"/><rect x="15" y="31" width="32" height="2"/><rect x="16" y="38" width="14" height="6"/><rect x="32" y="38" width="14" height="6"/><rect x="16" y="45" width="30" height="6"/></svg>
    </div>
    <p>Lorem ipsum dolor sit amet, consectetuer adipiscing elit,sed consectetuer adipiscing elit,sed diam nonummy.</p>
  </section>

  <footer>
    <div class="contact">
      <span><svg width="16" height="22" viewBox="0 0 16 22"><path d="M8 0a8 8 0 0 1 8 8c0 6-8 14-8 14S0 14 0 8a8 8 0 0 1 8-8z" fill="#fff"/><circle cx="8" cy="8" r="3" fill="#050505"/></svg>2400 Harbor Road Unit 4 Elmford, NJ 07100</span>
      <span><svg width="18" height="18" viewBox="0 0 18 18"><path d="M4 0l4 4-2 3c1 2 3 4 5 5l3-2 4 4-3 4C8 18 0 10 0 3z" fill="#fff"/></svg>555.310.4820</span>
      <span><svg width="20" height="14" viewBox="0 0 20 14"><rect width="20" height="14" fill="#fff"/><path d="M0 0l10 8 10-8" fill="none" stroke="#050505" stroke-width="1.6"/></svg>mvarela@rivolex.com</span>
      <span><svg width="18" height="18" viewBox="0 0 18 18"><circle cx="9" cy="9" r="9" fill="#fff"/><path d="M5 4c3 0 4 2 3 4s-3 1-3 4M12 10c2 0 2 3 0 5" stroke="#050505" stroke-width="2" fill="none"/></svg>www.rivolex.com</span>
    </div>
    <div class="legal">
      <p>Copyright 2017 info@rivolex.com. All rights reserved.</p>
      <div class="social"><i></i><i></i><i></i><i></i></div>
    </div>
  </footer>
</div>
</body>
</html>
```